Door Hanger Design

I need a design for a door hanger campaign. The door hanger will be 3.5" x 8.5" full color 2 sides. On the first side the emphasis is going to be house painting, exterior and interior. I would really like this to be bold and colorful, I would like to stay away from the standard here is what a painted house looks like.

For the 2nd side I would like the emphasis to be on kitchen and bathroom remodeling. One the front page of our website is a photo of one of our best jobs and if that could be incorporated into side 2 of the door hanger that would be awesome.

The name of our business is Dwelling Brightwell . Our website is http://dwelling-brightwell.example/. We don't currently have a company logo that we use.

I have never done this type of project before. So I'm sure I may be leaving some information out. If you need any questions answered please don't hesitate to contact me. They company that is going to print the designs said that I needed "camera ready artwork" and something about high resolution files.

Industry/Entity Type

House

```html
<!DOCTYPE html>
<html lang="en">
<head>
<meta charset="utf-8">
<title>Dwelling Brightwell Door Hangers</title>
<link href="https://fonts.googleapis.com/css2?family=Russo+One&family=Arimo:wght@400;700&display=swap" rel="stylesheet">
<style>
  :root {
    --paper: #ffffff;
    --hanger-yellow: #fff200;
    --hole: #000000;
    --red: #d7191f;
    --orange: #f26522;
    --purple: #6a2fb8;
    --blue: #1c3fd6;
    --green: #22d11e;
    --remodel-blue: #2f8fe0;
    --ink: #111111;
  }
  * { margin: 0; padding: 0; box-sizing: border-box; }
  html, body { width: 857px; height: 1200px; overflow: hidden; background: var(--paper); }
  .sheet { position: relative; width: 857px; height: 1200px; background: var(--paper); }
  .hanger {
    position: absolute; top: 116px; width: 378px; height: 982px;
    background: var(--hanger-yellow); overflow: hidden;
    font-family: "Arimo", Arial, sans-serif; color: var(--ink);
  }
  .hanger--remodel { left: 36px; }
  .hanger--painting { left: 443px; width: 382px; }
  .hanger__hole {
    position: absolute; top: 23px; width: 78px; height: 78px;
    border-radius: 50%; background: var(--hole); z-index: 3;
  }
  .hanger--remodel .hanger__hole { left: 157px; }
  .hanger--painting .hanger__hole { left: 154px; }

  .burst { position: absolute; left: 0; top: 0; width: 190px; height: 140px; z-index: 2; }
  .burst__text {
    position: absolute; left: 6px; top: 14px; width: 150px; z-index: 3;
    font-family: "Arimo", Arial, sans-serif; font-weight: 700; font-size: 29px;
    line-height: 31px; color: #fff; transform: rotate(-14deg); text-align: center;
  }

  .remodel-title {
    position: absolute; left: 0; right: 0; top: 150px; text-align: center;
    font-family: "Russo One", Impact, sans-serif; font-size: 41px; line-height: 47px;
    color: var(--remodel-blue); letter-spacing: 0.5px;
    -webkit-text-stroke: 1.5px #0b3a8a;
    text-shadow: 3px 3px 0 #fff, -2px -2px 0 #fff, 2px -2px 0 #fff, -2px 2px 0 #fff;
  }

  .photo { position: absolute; border: 7px solid var(--red); }
  .photo--featured { left: 32px; top: 264px; width: 310px; height: 236px;
    background: linear-gradient(180deg, #c9c4b8 0%, #7a3b2c 45%, #4a2a20 75%, #9a5a34 100%); }
  .photo--before { left: 169px; top: 512px; width: 170px; height: 125px;
    background: linear-gradient(180deg, #e6d2b0 0%, #c98a48 55%, #8d5a2e 100%); }
  .photo--after { left: 21px; top: 607px; width: 214px; height: 170px;
    background: linear-gradient(180deg, #b27a45 0%, #d49b5c 45%, #2b2b2b 80%, #7a7a7a 100%); }
  .photo-label { position: absolute; font-size: 14px; color: var(--ink); }
  .photo-label--before { left: 116px; top: 543px; }
  .photo-label--after { left: 250px; top: 712px; }

  .free-estimates {
    position: absolute; left: 0; right: 0; text-align: center;
    font-family: "Russo One", Impact, sans-serif; font-style: italic; color: var(--red);
    -webkit-text-stroke: 1px #000;
  }
  .hanger--remodel .free-estimates { top: 795px; font-size: 36px; }
  .hanger--painting .free-estimates { top: 792px; font-size: 30px; }
  .contact { position: absolute; left: 0; right: 0; text-align: center; }
  .contact__name { font-weight: 700; }
  .contact__phone { font-weight: 700; letter-spacing: 1px; }
  .contact__line { font-size: 15px; line-height: 20px; }
  .hanger--remodel .contact { top: 848px; }
  .hanger--remodel .contact__name { font-size: 20px; margin-bottom: 8px; }
  .hanger--remodel .contact__phone { font-size: 37px; line-height: 42px; margin-bottom: 6px; }
  .hanger--painting .contact { top: 832px; }
  .hanger--painting .contact__name { font-size: 19px; margin-bottom: 6px; }
  .hanger--painting .contact__phone { font-size: 32px; line-height: 36px; margin-bottom: 4px; }

  .stripes { position: absolute; left: 0; right: 0; display: flex; }
  .stripes--top { top: 0; height: 107px; }
  .stripes--bottom { bottom: 0; height: 32px; }
  .stripes span { flex: 1; }
  .c-orange { background: var(--orange); } .c-red { background: var(--red); }
  .c-purple { background: var(--purple); } .c-blue { background: var(--blue); }
  .c-green { background: var(--green); }

  .painting-kicker {
    position: absolute; left: 20px; top: 150px; font-family: "Arimo", Arial, sans-serif;
    font-weight: 700; font-size: 17px; color: var(--ink);
  }
  .painting-title {
    position: absolute; left: 28px; top: 180px; font-family: "Russo One", Impact, sans-serif;
    font-size: 62px; line-height: 62px; -webkit-text-stroke: 2px #000;
    text-shadow: 4px 4px 0 #fff;
  }
  .painting-title .word { display: block; }
  .painting-title .word--second { margin-left: 10px; transform: rotate(-6deg); transform-origin: left; }
  .t-red { color: var(--red); } .t-orange { color: var(--orange); } .t-yellow { color: #ffe600; }
  .t-green { color: var(--green); } .t-blue { color: var(--blue); } .t-purple { color: var(--purple); }

  .brushes {
    position: absolute; left: 92px; top: 304px; width: 290px; height: 474px;
    background: repeating-linear-gradient(180deg,
      #ffe600 0 60px, transparent 60px 78px,
      #f26522 78px 138px, transparent 138px 156px,
      #d7191f 156px 216px, transparent 216px 234px,
      #6a2fb8 234px 294px, transparent 294px 312px,
      #1c3fd6 312px 372px, transparent 372px 390px,
      #22d11e 390px 450px, transparent 450px 474px);
    opacity: 0.85;
  }
</style>
</head>
<body>
<main class="sheet">

  <section class="hanger hanger--remodel" aria-label="Kitchen and bath remodeling side">
    <div class="hanger__hole"></div>
    <svg class="burst" viewBox="0 0 190 140" aria-hidden="true">
      <polygon fill="#d7191f" points="0,0 190,0 150,30 185,48 128,62 150,92 100,86 96,125 66,98 38,135 30,100 0,112"/>
    </svg>
    <p class="burst__text">We Also Offer</p>

    <h2 class="remodel-title">KITCHEN &amp; BATH<br>REMODELING</h2>

    <div class="photo photo--featured" role="img" aria-label="Photo of a finished kitchen with dark cabinets and island"></div>
    <span class="photo-label photo-label--before">BEFORE</span>
    <div class="photo photo--before" role="img" aria-label="Photo of a kitchen before remodeling"></div>
    <div class="photo photo--after" role="img" aria-label="Photo of the kitchen after remodeling"></div>
    <span class="photo-label photo-label--after">AFTER</span>

    <p class="free-estimates">FREE ESTIMATES!</p>
    <div class="contact">
      <p class="contact__name">Contact Marcus Delaney</p>
      <p class="contact__phone">555-018-4472</p>
      <p class="contact__line">e-mail: marcus@dwelling-brightwell.example</p>
      <p class="contact__line">www.dwelling-brightwell.example</p>
    </div>
  </section>

  <section class="hanger hanger--painting" aria-label="House painting side">
    <div class="stripes stripes--top">
      <span class="c-orange"></span><span class="c-red"></span><span class="c-purple"></span><span class="c-blue"></span><span class="c-green"></span>
    </div>
    <div class="hanger__hole"></div>

    <p class="painting-kicker">INTERIOR or EXTERIOR</p>
    <h1 class="painting-title">
      <span class="word"><span class="t-red">H</span><span class="t-orange">O</span><span class="t-yellow">U</span><span class="t-green">S</span><span class="t-blue">E</span></span>
      <span class="word word--second"><span class="t-purple">P</span><span class="t-yellow">A</span><span class="t-orange">I</span><span class="t-red">N</span><span class="t-green">T</span><span class="t-blue">I</span><span class="t-purple">N</span><span class="t-red">G</span></span>
    </h1>

    <div class="brushes" role="img" aria-label="Illustration of six paintbrushes dripping yellow, orange, red, purple, blue and green paint"></div>

    <p class="free-estimates">FREE ESTIMATES!</p>
    <div class="contact">
      <p class="contact__name">Contact Marcus Delaney</p>
      <p class="contact__phone">555-018-4472</p>
      <p class="contact__line">e-mail: marcus@dwelling-brightwell.example</p>
      <p class="contact__line">www.dwelling-brightwell.example</p>
    </div>

    <div class="stripes stripes--bottom">
      <span class="c-orange"></span><span class="c-red"></span><span class="c-purple"></span><span class="c-blue"></span><span class="c-green"></span>
    </div>
  </section>

</main>
</body>
</html>
```